Lantern Hill Publicity is a new boutique Press Office with a small roster of well-chosen clients across an array of disciplines; from Art and Technology to Restaurants and Fashion. Based in Greenpoint Brooklyn, Lantern Hill Publicity achieves outstanding results through hard work, tenacity, efficiency and a sense of humor. We need a simple, versatile and classic design. We would like each side of the card to be white text on a black background.

Boutique

```html
<!DOCTYPE html>
<html lang="en">
<head>
<meta charset="utf-8">
<title>Lantern Hill Publicity — Business Card</title>
<link rel="stylesheet" href="https://fonts.googleapis.com/css2?family=Source+Sans+3:wght@400&display=swap">
<style>
  :root {
    --backdrop: #eef3f1;
    --card: #05050a;
    --ink: #ffffff;
    --ink-soft: #e6e6e6;
  }
  * { box-sizing: border-box; margin: 0; padding: 0; }
  html, body {
    width: 1200px;
    height: 608px;
    overflow: hidden;
    background: var(--backdrop);
    font-family: "Source Sans 3", "Calibri", sans-serif;
    color: var(--ink);
  }
  .stage { position: relative; width: 1200px; height: 608px; }
  .card {
    position: absolute;
    top: 161px;
    width: 504px;
    height: 285px;
    background: var(--card);
  }
  .card--front { left: 90px; }
  .card--back { left: 606px; }

  .wordmark {
    position: absolute;
    text-align: center;
    font-weight: 400;
    text-transform: uppercase;
    color: var(--ink);
    line-height: 1.3;
  }
  .card--front .wordmark {
    left: 12px;
    width: 240px;
    top: 112px;
    font-size: 19px;
    letter-spacing: 0.18em;
  }
  .card--back .wordmark {
    left: 0;
    width: 504px;
    top: 104px;
    font-size: 30px;
    letter-spacing: 0.2em;
  }

  .contact {
    position: absolute;
    right: 29px;
    top: 111px;
    text-align: right;
  }
  .contact__name { font-size: 15.5px; line-height: 20px; }
  .contact__role { font-size: 10px; line-height: 14px; margin-top: 3px; color: var(--ink-soft); }
  .contact__line { font-size: 11.5px; line-height: 15px; }
  .contact__line--phone { margin-top: 41px; }
  .contact__line--email { margin-top: 9px; }
  .contact__line--address { margin-top: 11px; font-size: 10px; }
</style>
</head>
<body>
  <main class="stage">
    <section class="card card--front" aria-label="Card front">
      <div class="wordmark">Lantern Hill<br>Publicity</div>
      <div class="contact">
        <p class="contact__name">Daniel Marchetti</p>
        <p class="contact__role">Owner &amp; Founder</p>
        <p class="contact__line contact__line--phone">Mobile: 917-555-0148</p>
        <p class="contact__line contact__line--email">Email: daniel@lanternhillpr.com</p>
        <p class="contact__line contact__line--address">LLC 84 Calyer Street Unit 3 Brooklyn, NY 11222</p>
      </div>
    </section>
    <section class="card card--back" aria-label="Card back">
      <div class="wordmark">Lantern Hill<br>Publicity</div>
    </section>
  </main>
</body>
</html>
```